creation of business cards for Velanto Sàrl

Velanto S% 26 # 224; rl is a soci% 26 # 233; t% 26 # 233; consultancy that accompanies companies in the development of their business on the market% 26 # 233; Switzerland by providing strategic contacts or market information; and by providing administrative or logistical support. Our consulting skills focus on sectors% 26 # 224; high value added% 26 # 233; e, such as trade in food goods% 26 # 39amp; drinks, fashion% 26amp; lifestyle, products and services for% 26 # 233; s in high-tech industries (pharmaceutical, chemical, m% 26 # 233; pricy 26% 23 #; cision) or sustainable solutions (% 26 # 233; energies renewable, mat% 26 # 233; recyclable materials). As part of the launch of our activity% 26 # 233;, we need% 26 # 39;% 26 # 233; to establish business cards to d% 26 # 233; work our new customers (Swiss or international).

Target Market(s)

Companies wishing to develop their activity% 26 # 233; s in Switzerland or% 26 # 224; l% 26 # 39;% 26 # 233; abroad (mainly in Europe).

Contact Information for Business Card

Prénom NOM
Velanto Sàrl
Bureau de Marvoisin
Rue des Tilleuls 47, 2000 Neuchâtel
Tél. : 032 718 46 39
info@velanto-example.ch
www.velanto-example.ch

Font styles to use
Serif
Sans Serif

Colors

Designer to choose colors to be used in the design.

Requirements
Must have
• The logo The name of the company% 26 # 233; t% 26 # 233; (Velanto S% 26 # 224; rl) One field for the mailing address One field for the number% 26 # 233; ro de t% 26 # 233; l% 26 # 233; phone One field for the % 26 # 39; email address and website

```html
<!DOCTYPE html>
<html lang="fr">
<head>
<meta charset="utf-8">
<title>Velanto Sàrl – cartes de visite</title>
<link rel="stylesheet" href="https://fonts.googleapis.com/css2?family=Michroma&family=Arimo:wght@400;700&display=swap">
<style>
  :root {
    --bg: #2a2a2b;
    --card-white: #ffffff;
    --card-black: #1b1c1e;
    --navy: #1f3b53;
    --ink: #1a1a1a;
    --rule: #9a9a9a;
    --pattern-a: #232427;
    --pattern-b: #18191b;
  }
  * { box-sizing: border-box; margin: 0; padding: 0; }
  html, body { width: 1200px; height: 1108px; overflow: hidden; }
  body {
    background: var(--bg);
    font-family: "Arimo", Arial, sans-serif;
    position: relative;
  }
  .card {
    position: absolute;
    top: 234px;
    width: 400px;
    height: 640px;
    border-radius: 26px;
    overflow: hidden;
  }
  .card-front { left: 160px; background: var(--card-white); color: var(--ink); text-align: center; }
  .card-back { left: 640px; background: var(--card-black); }

  .brand {
    position: absolute;
    top: 120px;
    left: 0; right: 0;
    display: flex;
    align-items: center;
    justify-content: center;
    gap: 16px;
  }
  .brand-square {
    width: 44px; height: 44px;
    border-radius: 9px;
    background: var(--navy);
  }
  .brand-name {
    font-family: "Michroma", Arial, sans-serif;
    font-size: 34px;
    color: var(--navy);
    letter-spacing: 1px;
  }
  .person-name {
    position: absolute;
    top: 318px; left: 0; right: 0;
    font-family: "Michroma", Arial, sans-serif;
    font-size: 21px;
    color: var(--navy);
  }
  .icon-rule {
    position: absolute;
    top: 370px; left: 60px; right: 60px;
    display: flex;
    align-items: center;
    gap: 8px;
  }
  .icon-rule .line { flex: 1; height: 1px; background: var(--rule); }
  .icon-rule svg { width: 24px; height: 24px; display: block; }
  .contact {
    position: absolute;
    top: 410px; left: 0; right: 0;
    font-size: 17px;
    line-height: 23px;
  }
  .divider {
    position: absolute;
    top: 488px; left: 90px; right: 90px;
    height: 1px; background: var(--rule);
  }
  .address {
    position: absolute;
    top: 500px; left: 0; right: 0;
    font-size: 17px;
    line-height: 23px;
  }
  .address .company { font-weight: 700; }

  .pattern-field {
    position: absolute; inset: 0;
    background: linear-gradient(160deg, var(--pattern-a) 0%, var(--pattern-b) 75%);
  }
  .back-mark {
    position: absolute;
    left: 180px; top: 494px;
    width: 40px; height: 40px;
    border: 2px solid #d9d9d9;
    border-radius: 6px;
  }
</style>
</head>
<body>
  <section class="card card-front">
    <div class="brand">
      <span class="brand-square"></span>
      <span class="brand-name">VELANTO</span>
    </div>
    <div class="person-name">PRENOM NOM</div>
    <div class="icon-rule">
      <span class="line"></span>
      <svg viewBox="0 0 24 24" aria-label="Téléphone"><rect width="24" height="24" rx="4" fill="#1f3b53"/><path d="M8 6c1 0 2 2 2 3s-1 1-1 2 2 3 3 3 1-1 2-1 3 1 3 2-1 2-2 2c-4 0-9-5-9-9 0-1 1-2 2-2z" fill="#fff"/></svg>
      <svg viewBox="0 0 24 24" aria-label="E-mail"><rect width="24" height="24" rx="4" fill="#1f3b53"/><rect x="5" y="7" width="14" height="10" fill="none" stroke="#fff" stroke-width="1.5"/><path d="M5 7l7 6 7-6" fill="none" stroke="#fff" stroke-width="1.5"/></svg>
      <svg viewBox="0 0 24 24" aria-label="Site web"><rect width="24" height="24" rx="4" fill="#1f3b53"/><path d="M12 5a5 5 0 0 1 5 5c0 4-5 9-5 9s-5-5-5-9a5 5 0 0 1 5-5z" fill="#fff"/><circle cx="12" cy="10" r="2" fill="#1f3b53"/></svg>
      <span class="line"></span>
    </div>
    <div class="contact">
      <p>032 718 46 39</p>
      <p>info@velanto-example.ch</p>
      <p>www.velanto-example.ch</p>
    </div>
    <div class="divider"></div>
    <div class="address">
      <p class="company">VELANTO SÀRL</p>
      <p>Bureau de Marvoisin</p>
      <p>Rue des Tilleuls 47, 2000 Neuchâtel</p>
    </div>
  </section>

  <section class="card card-back">
    <div class="pattern-field" role="img" aria-label="Motif ton sur ton répété de la marque Velanto sur fond noir"></div>
    <div class="back-mark"></div>
  </section>
</body>
</html>
```